Breezeway Climate Business Card Design

Design new, 2 sides, business cards for a residential and light commercial heating, air conditioning contractor.

Target Market(s)

Homeowners, small businesses

Industry/Entity Type

Business

Contact Information for Business Card

Dominic Vasquerelli
Phone - 555-214-6837
Email
Address - PO box 618
Millbrook NJ 07999
Website - www.BreezewayClimateLLC.example

Requirements
Must have
• logo, company colors, standard size with no die cut, so I can use printhaven

```html
<!DOCTYPE html>
<html lang="en">
<head>
<meta charset="utf-8">
<title>Breezeway Climate Business Card</title>
<link href="https://fonts.googleapis.com/css2?family=Roboto+Condensed:wght@400;700&display=swap" rel="stylesheet">
<style>
  :root {
    --bg: #e9e7e6;
    --card: #ffffff;
    --orange: #f57a14;
    --crimson: #a3151c;
    --black: #111111;
    --red: #e8101a;
    --field: #e4e4e4;
    --ink: #1d1d1d;
    --rule: #9a9a9a;
  }
  * { box-sizing: border-box; margin: 0; padding: 0; }
  html, body { width: 1200px; height: 800px; overflow: hidden; }
  body {
    background: var(--bg);
    font-family: "Roboto Condensed", Arial, sans-serif;
    position: relative;
  }
  .card {
    position: absolute;
    top: 252px;
    width: 520px;
    height: 297px;
    background: var(--card);
    box-shadow: 0 6px 18px rgba(0,0,0,.18);
    overflow: hidden;
  }
  .card--front { left: 53px; }
  .card--back { left: 627px; }

  /* Front */
  .front-band {
    position: absolute;
    top: 112px;
    height: 74px;
    background: var(--orange);
  }
  .front-band--left { left: 0; width: 150px; clip-path: polygon(0 0, 100% 0, 82% 100%, 0 100%); }
  .front-band--right { right: 0; width: 150px; clip-path: polygon(18% 0, 100% 0, 100% 100%, 0 100%); }
  .wordmark {
    position: absolute;
    left: 0; right: 0;
    top: 128px;
    text-align: center;
    font-weight: 700;
    font-size: 36px;
    letter-spacing: 1px;
    text-transform: uppercase;
    color: var(--crimson);
    line-height: 42px;
  }

  /* Back */
  .holder { position: absolute; left: 34px; top: 26px; }
  .holder-name { font-weight: 700; font-size: 17px; color: var(--ink); letter-spacing: .3px; }
  .holder-role { font-size: 10px; letter-spacing: 2px; color: #444; margin-top: 1px; }
  .holder-rule { position: absolute; left: 34px; right: 30px; top: 70px; height: 1px; background: var(--rule); }
  .contact {
    position: absolute;
    display: flex;
    align-items: center;
    height: 22px;
  }
  .contact-icon {
    width: 26px; height: 22px;
    background: var(--crimson);
    display: flex; align-items: center; justify-content: center;
    clip-path: polygon(0 0, 78% 0, 100% 50%, 78% 100%, 0 100%);
  }
  .contact-text {
    height: 18px;
    width: 170px;
    margin-left: 4px;
    background: var(--field);
    font-size: 11px;
    line-height: 18px;
    padding-left: 8px;
    color: var(--ink);
  }
  .contact--phone { left: 34px; top: 88px; }
  .contact--email { left: 34px; top: 124px; }
  .contact--web { left: 280px; top: 88px; }
  .contact--address { left: 280px; top: 124px; }

  .back-band {
    position: absolute; left: 0; right: 0; top: 168px; height: 62px;
    background: var(--orange);
    display: flex; flex-direction: column; justify-content: center; align-items: center;
  }
  .tagline {
    color: #fff;
    font-size: 13px;
    line-height: 16px;
    text-transform: uppercase;
    text-align: center;
    letter-spacing: .3px;
  }
  .back-stripe { position: absolute; left: 0; right: 0; top: 230px; height: 16px; background: var(--black); }
  .back-stripe-accent { position: absolute; left: 372px; top: 230px; width: 52px; height: 16px; background: var(--red); }
</style>
</head>
<body>
  <section class="card card--front" aria-label="Card front">
    <div class="front-band front-band--left"></div>
    <div class="front-band front-band--right"></div>
    <div class="wordmark">Breezeway Climate</div>
  </section>

  <section class="card card--back" aria-label="Card back">
    <div class="holder">
      <div class="holder-name">CARD HOLDER NAME</div>
      <div class="holder-role">DESIGNATION</div>
    </div>
    <div class="holder-rule"></div>

    <div class="contact contact--phone">
      <span class="contact-icon">
        <svg width="12" height="12" viewBox="0 0 24 24" fill="none" stroke="#fff" stroke-width="2.2"><path d="M5 3h4l2 5-3 2a11 11 0 0 0 6 6l2-3 5 2v4a2 2 0 0 1-2 2A17 17 0 0 1 3 5a2 2 0 0 1 2-2z"/></svg>
      </span>
      <span class="contact-text">000 1234 5556</span>
    </div>
    <div class="contact contact--email">
      <span class="contact-icon">
        <svg width="13" height="11" viewBox="0 0 24 18" fill="none" stroke="#fff" stroke-width="2"><rect x="1" y="1" width="22" height="16"/><path d="M1 1l11 9 11-9"/></svg>
      </span>
      <span class="contact-text">yourid@domain.example</span>
    </div>
    <div class="contact contact--web">
      <span class="contact-icon">
        <svg width="12" height="12" viewBox="0 0 24 24" fill="none" stroke="#fff" stroke-width="2"><circle cx="12" cy="12" r="10"/><path d="M2 12h20M12 2a15 15 0 0 1 0 20M12 2a15 15 0 0 0 0 20"/></svg>
      </span>
      <span class="contact-text">www.yourwebsite.example</span>
    </div>
    <div class="contact contact--address">
      <span class="contact-icon">
        <svg width="10" height="13" viewBox="0 0 18 24" fill="none" stroke="#fff" stroke-width="2.2"><path d="M9 23s7-8 7-14A7 7 0 0 0 2 9c0 6 7 14 7 14z"/><circle cx="9" cy="9" r="2.5"/></svg>
      </span>
      <span class="contact-text">your street address here</span>
    </div>

    <div class="back-band">
      <p class="tagline">Residential and light commercial heating<br>air conditioning contractor</p>
    </div>
    <div class="back-stripe"></div>
    <div class="back-stripe-accent"></div>
  </section>
</body>
</html>
```